Brimble Diecast Torvel Collectables Website

looking for a vibrant web site marketplace built for diecast car enthusiasts to buy, sell, and trade with ease. Whether you're looking to showcase your own collection or discover rare and exciting models, our site makes the process simple and enjoyable. Clients can browse a curated inventory of high‑quality diecast cars, connect with fellow collectors, and find the perfect pieces to expand their collection. With a smooth user experience and a community-driven spirit, we’re the go‑to destination for anyone passionate about diecast cars.

Target Market(s)

diecast collectors

Industry/Entity Type

Diecast Collectables

Coding

Coded - Design and coding required

Number of Pages Required

3 page

Font styles to use
Sans Serif

Colors
EE7325
F08F49
F5BC92
FAE3D3
FDF4ED

Requirements
Must have
• Cool look and feel. Woo commerce page to post and sell my inventory
Nice to have
• page for users to post their cars or looking for trades.
Should not have
• look cheap

```html
<!DOCTYPE html>
<html lang="en">
<head>
<meta charset="utf-8">
<title>Brimble Diecast — Where Collectors Race to Find the Rare</title>
<link href="https://fonts.googleapis.com/css2?family=Playfair+Display:ital,wght@0,800;0,900;1,900&family=Archivo:wght@400;600;700;800&display=swap" rel="stylesheet">
<style>
:root{
  --ink:#1f1f1f;
  --ink-2:#262626;
  --cream:#e8d8b4;
  --cream-2:#f1e5c9;
  --orange:#c9572b;
  --red:#d8493a;
  --green:#2e5240;
  --green-2:#2a4b3a;
  --muted:#8b8a86;
  --line:#4a4a48;
  --serif:"Playfair Display", Georgia, serif;
  --sans:"Archivo", Arial, sans-serif;
}
*{box-sizing:border-box;margin:0;padding:0}
html,body{width:1200px;height:4488px;overflow:hidden;background:var(--ink);color:var(--cream);font-family:var(--sans)}
.abs{position:absolute}
section,header,footer{position:relative;width:1200px;overflow:hidden}
.display{font-family:var(--serif);font-weight:900;letter-spacing:-2px;text-transform:uppercase;line-height:1}
.label{font-family:var(--sans);font-weight:700;text-transform:uppercase;letter-spacing:3px;font-size:10px}
.btn{display:flex;align-items:center;justify-content:center;font-family:var(--sans);font-weight:800;text-transform:uppercase;letter-spacing:2.5px;font-size:11px}

/* hero */
.hero{height:862px;border-bottom:7px solid var(--green)}
.hero-scene{inset:0;background:
  linear-gradient(180deg,rgba(20,30,32,.35) 0%,rgba(20,20,20,0) 30%,rgba(25,18,14,.6) 100%),
  radial-gradient(ellipse 55% 40% at 75% 35%,#8a4a2c 0%,rgba(138,74,44,0) 70%),
  linear-gradient(180deg,#2d4a52 0%,#6b7a78 14%,#4a3a34 32%,#6e3a24 55%,#3a2218 80%,#1e1714 100%)}
.nav{top:0;left:0;width:1200px;height:57px;background:rgba(31,31,31,.92);border-bottom:2px solid #3a3a38}
.nav-links{left:0;right:0;top:20px;display:flex;justify-content:center;gap:28px}
.nav-links a{color:var(--cream);text-decoration:none;font-weight:800;font-size:12px;letter-spacing:2px;padding-bottom:5px}
.nav-links a.active{border-bottom:2px solid var(--orange)}
.brand{top:18px;left:86px;display:flex;align-items:center;gap:8px;font-family:var(--serif);font-weight:900;font-size:20px;color:var(--cream);text-transform:uppercase}
.brand i{width:12px;height:12px;border-radius:50%;background:var(--orange);display:block}
.nav-icons{right:36px;top:18px;display:flex;gap:32px}
.chip{height:19px;padding:0 10px;display:flex;align-items:center;font-size:9px;font-weight:800;letter-spacing:2.5px;text-transform:uppercase}
.hero h1{left:62px;top:232px;font-size:90px;line-height:75px;color:var(--cream);letter-spacing:-3px}
.hero h1 em{color:var(--red);font-style:italic}
.btn-explore{left:62px;top:634px;width:246px;height:54px;background:var(--orange);color:var(--cream);box-shadow:0 4px 0 #8a3514}
.btn-sell{left:62px;top:704px;width:271px;height:54px;border:2px solid var(--cream);color:var(--cream)}

/* new at the pit */
.pit{height:775px;background:var(--ink);border-bottom:7px solid var(--green)}
.pit .kicker{left:21px;top:86px;color:var(--orange);font-size:10px}
.pit h2{left:21px;top:100px;font-size:44px;color:var(--cream)}
.btn-outline{border:2px solid var(--cream);color:var(--cream);font-size:10px}
.divider{left:21px;right:21px;height:1px;background:var(--line)}
.card{width:362px;height:448px;border:3px solid var(--orange);top:232px}
.card .ph{left:22px;top:22px;right:22px;height:209px;border:1px solid #555}
.card .tag{top:-14px;right:-4px;height:24px;padding:0 11px;font-size:9px;letter-spacing:1px;font-weight:800;display:flex;align-items:center;text-transform:uppercase}
.card h3{left:22px;right:22px;top:252px;font-family:var(--serif);font-weight:800;font-size:20px;color:var(--cream);letter-spacing:-.5px;text-transform:uppercase;white-space:nowrap}
.card .meta{left:22px;top:312px;font-size:9px;letter-spacing:2px;color:var(--muted);font-weight:700;text-transform:uppercase}
.card .price{left:22px;top:329px;font-family:var(--sans);font-weight:800;font-style:italic;font-size:26px;color:var(--orange)}
.card .specs{right:22px;top:318px;display:flex;flex-direction:column;align-items:flex-end;gap:6px}
.spec{font-size:7px;font-weight:800;letter-spacing:1px;padding:3px 7px;text-transform:uppercase}
.spec.fill{background:var(--cream);color:var(--ink)}
.spec.out{border:1px solid var(--cream);color:var(--cream)}
.card .cart{left:22px;right:22px;top:383px;height:35px;background:var(--orange);color:var(--cream);font-size:10px}

/* pick your track */
.track{height:421px;background:var(--cream)}
.track h2{left:0;right:0;top:96px;text-align:center;font-size:42px;color:var(--ink)}
.track .rule{top:122px;height:3px;background:var(--ink)}
.tile{top:181px;width:214px;height:155px;border:3px solid var(--ink);box-shadow:9px 9px 0 var(--ink);display:flex;flex-direction:column;align-items:center;justify-content:center;gap:14px;font-family:var(--serif);font-weight:800;font-size:17px;text-transform:uppercase;letter-spacing:-.5px}
.tile .dot{width:5px;height:5px;border-radius:50%;background:currentColor;position:absolute}

/* commander */
.cmd{height:833px;background:var(--ink);border-bottom:10px solid var(--orange)}
.cmd .badge{left:21px;top:132px;height:24px;padding:0 16px;background:var(--orange);border:2px solid #e27d4d;outline:2px solid var(--orange);color:var(--cream);font-size:9px}
.cmd h2{left:21px;top:192px;font-size:68px;line-height:63px;color:var(--cream)}
.cmd .lede{left:21px;top:482px;padding-left:22px;border-left:3px solid var(--orange);font-size:17px;line-height:24px;color:#b8b5ac;width:460px}
.feat{top:587px;width:206px;height:134px;border:1px solid #474745;padding:24px 22px}
.feat h4{font-size:10px;letter-spacing:2px;font-weight:800;display:flex;gap:10px;align-items:center;margin-bottom:14px;text-transform:uppercase}
.feat p{font-size:12px;line-height:18px;color:#6e6d69}
.review{padding:26px 30px}
.review .who{display:flex;gap:14px;align-items:center}
.review .av{width:40px;height:38px;display:flex;align-items:center;justify-content:center;font-weight:800;font-size:15px}
.review .handle{font-weight:800;font-size:12px}
.review .role{font-size:8px;letter-spacing:1px;margin-top:6px;font-weight:700;text-transform:uppercase}
.review .stars{position:absolute;right:30px;top:22px;font-size:14px;letter-spacing:2px}
.review blockquote{margin-top:22px;font-style:italic;font-weight:700;font-size:15px;line-height:22px}
.r1{left:533px;top:222px;width:447px;height:200px;background:var(--cream);border:3px solid var(--red);color:var(--ink);transform:rotate(-2deg)}
.r2{left:733px;top:437px;width:446px;height:197px;background:var(--ink);border:3px solid var(--cream);box-shadow:10px 10px 0 var(--orange);color:var(--cream);transform:rotate(1.5deg)}

/* garage */
.garage{height:712px;background:var(--green);border-bottom:10px solid var(--orange)}
.garage h2{left:21px;top:90px;font-size:42px;font-style:italic;color:var(--cream)}
.garage .sub{left:21px;top:150px;font-size:10px;letter-spacing:3.5px;font-weight:700;color:#b9c3b2;text-transform:uppercase}
.post{width:272px;height:340px;border:3px solid #1c1c1c;box-shadow:0 8px 14px rgba(0,0,0,.35)}
.post .ph{inset:0}
.post .cap{left:22px;right:22px;bottom:24px}
.post .cat{font-size:9px;letter-spacing:3px;font-weight:800;color:var(--orange);text-transform:uppercase;margin-bottom:6px}
.post h3{font-family:var(--serif);font-weight:900;font-size:22px;line-height:24px;color:var(--cream);text-transform:uppercase}

/* join */
.join{height:690px;background:var(--ink);border-bottom:6px solid var(--green)}
.join .shadow{left:230px;top:136px;width:782px;height:456px;background:var(--orange)}
.join .corner{left:186px;top:95px;width:72px;height:72px;border-left:6px solid var(--orange);border-top:6px solid var(--orange)}
.join .box{left:209px;top:115px;width:782px;height:456px;background:var(--ink);border:3px solid var(--cream)}
.join .kicker{left:0;right:0;top:89px;text-align:center;color:var(--orange);font-size:10px;letter-spacing:5px}
.join h2{left:0;right:0;top:116px;text-align:center;font-size:70px;color:var(--cream)}
.join p{left:120px;right:120px;top:204px;text-align:center;font-size:11px;line-height:20px;letter-spacing:1.5px;color:#9b988f;text-transform:uppercase}
.join .field{left:70px;top:278px;width:637px;height:66px;border:3px solid var(--cream);display:flex}
.join .field span{flex:1;display:flex;align-items:center;padding-left:22px;font-size:11px;letter-spacing:2px;font-weight:700;color:#55544f;text-transform:uppercase}
.join .field b{width:208px;background:var(--cream);color:var(--ink);display:flex;align-items:center;justify-content:center;font-size:13px;letter-spacing:4px;font-weight:800}
.join .perks{left:0;right:0;top:380px;display:flex;justify-content:center;gap:26px;font-size:8px;letter-spacing:1px;font-weight:800;color:var(--green);text-transform:uppercase}
.join .perks span{display:flex;align-items:center;gap:6px}

/* footer */
.foot{height:172px;background:var(--ink)}
.foot .fb{left:21px;top:60px;font-family:var(--serif);font-weight:900;font-style:italic;font-size:28px;color:var(--orange);text-transform:uppercase}
.foot .copy{left:21px;top:104px;font-size:8px;letter-spacing:3px;color:#6e6d69;font-weight:700;text-transform:uppercase}
.foot .links{left:444px;top:84px;display:flex;gap:36px;font-size:9px;letter-spacing:1.5px;font-weight:800;color:#8b8a86;text-transform:uppercase}
.foot .social{right:30px;top:80px;display:flex;gap:20px}
.foot .social i{display:block;width:14px;height:14px;border-radius:50%;border:2px solid #6e6d69}
</style>
</head>
<body>

<header class="hero">
  <div class="abs hero-scene" role="img" aria-label="Rally diecast car kicking up dust on a desert canyon road at dusk"></div>
  <nav class="abs nav">
    <div class="abs brand"><i></i>Brimble Diecast</div>
    <div class="abs nav-links"><a class="active" href="#">SHOP</a><a href="#">SELL</a><a href="#">GARAGE</a></div>
    <div class="abs nav-icons">
      <svg width="16" height="16" viewBox="0 0 16 16" fill="none" stroke="#e8d8b4" stroke-width="2"><circle cx="6.5" cy="6.5" r="4.5"/><path d="M10 10l4.5 4.5"/></svg>
      <svg width="18" height="16" viewBox="0 0 18 16" fill="#e8d8b4"><path d="M0 0h3l3 9h9l2-7H5l-.6-2H0z"/><circle cx="7" cy="13.5" r="1.8"/><circle cx="14" cy="13.5" r="1.8"/></svg>
    </div>
  </nav>
  <div class="abs chip" style="left:64px;top:173px;background:var(--green);color:var(--cream);border:1px solid #6f8f72">1,200+ Verified Collectors</div>
  <div class="abs chip" style="left:64px;top:201px;background:var(--orange);color:var(--cream)">New Drops Weekly</div>
  <h1 class="abs display">Where<br>Collectors<br><em>Race</em><br>&nbsp;To Find<br>The Rare</h1>
  <a class="abs btn btn-explore">Explore Inventory</a>
  <a class="abs btn btn-sell">Sell Your Collection</a>
</header>

<section class="pit">
  <div class="abs label kicker">Data Feed: Live Listings</div>
  <h2 class="abs display">New at the Pit</h2>
  <a class="abs btn btn-outline" style="left:1010px;top:110px;width:167px;height:37px">Full Inventory &nbsp;
    <svg width="11" height="9" viewBox="0 0 11 9" fill="none" stroke="#e8d8b4" stroke-width="1.4"><rect x=".7" y=".7" width="9.6" height="7.6"/><path d="M3 3h5"/></svg></a>
  <div class="abs divider" style="top:176px"></div>

  <article class="abs card" style="left:21px">
    <div class="abs ph" role="img" aria-label="Maroon 1969 muscle car model, close-up of the hood" style="background:linear-gradient(160deg,#3a2a26 0%,#5a1e22 45%,#2a1a18 100%)"></div>
    <div class="abs spec fill" style="left:32px;top:208px;background:var(--green);color:var(--cream)">Trending</div>
    <div class="abs tag" style="background:var(--red);color:var(--cream);border:2px solid var(--cream)">1 of 500</div>
    <h3 class="abs">1969 Raptor Fastback 440</h3>
    <div class="abs meta">Last sold: $210</div>
    <div class="abs price">$185.00</div>
    <div class="abs specs"><span class="spec fill">Scale 1:18</span><span class="spec out">Original Box</span></div>
    <a class="abs btn cart">Add to Cart</a>
  </article>

  <article class="abs card" style="left:419px">
    <div class="abs ph" role="img" aria-label="Silver and yellow number 12 stock car model on a dark surface" style="background:linear-gradient(160deg,#3a3a3a 0%,#9a9a94 45%,#b6ad52 60%,#2c2c2c 100%)"></div>
    <div class="abs tag" style="background:var(--green);color:var(--cream);border:2px solid var(--cream)">Rare Track Find</div>
    <h3 class="abs">Torvel Series 7 Stock Car</h3>
    <div class="abs meta">Last sold: $72</div>
    <div class="abs price">$64.50</div>
    <div class="abs specs"><span class="spec fill">Scale 1:24</span><span class="spec out">Authorized</span></div>
    <a class="abs btn cart">Add to Cart</a>
  </article>

  <article class="abs card" style="left:817px">
    <div class="abs ph" role="img" aria-label="Blue custom hot rod model with flame decals" style="background:linear-gradient(160deg,#1a1a1c 0%,#1f3f8a 45%,#2a56b0 60%,#141414 100%)"></div>
    <div class="abs tag" style="background:var(--cream);color:var(--ink);border:2px solid var(--ink)">One-off Build</div>
    <h3 class="abs">Custom '32 Ardent Roadster</h3>
    <div class="abs meta">Rarity rank: S+</div>
    <div class="abs price">$120.00</div>
    <div class="abs specs"><span class="spec fill">Scale 1:24</span><span class="spec out">Hand Built</span></div>
    <a class="abs btn cart">Add to Cart</a>
  </article>
</section>

<section class="track">
  <div class="abs rule" style="left:21px;width:364px"></div>
  <h2 class="abs display">Pick Your Track</h2>
  <div class="abs rule" style="left:816px;width:363px"></div>

  <div class="abs tile" style="left:21px;background:var(--cream);color:var(--ink)">
    <i class="dot" style="left:8px;top:8px"></i><i class="dot" style="right:8px;top:8px"></i><i class="dot" style="left:8px;bottom:8px"></i><i class="dot" style="right:8px;bottom:8px"></i>
    <svg width="26" height="28" viewBox="0 0 26 28"><path d="M3 2v25" stroke="#1f1f1f" stroke-width="2.5"/><path d="M4 3h19v13H4z" fill="#fff" stroke="#1f1f1f" stroke-width="1.5"/><path d="M4 3h5v4H4zM14 3h5v4h-5zM9 7h5v4H9zM19 7h4v4h-4zM4 11h5v5H4zM14 11h5v5h-5z" fill="#1f1f1f"/></svg>
    Torvel</div>
  <div class="abs tile" style="left:257px;background:var(--cream);color:var(--ink)">
    <i class="dot" style="left:8px;top:8px"></i><i class="dot" style="right:8px;top:8px"></i><i class="dot" style="left:8px;bottom:8px"></i><i class="dot" style="right:8px;bottom:8px"></i>
    <svg width="30" height="30" viewBox="0 0 30 30"><circle cx="15" cy="15" r="14" fill="#1f1f1f"/><path d="M15 6l2.6 5.8 6.3.6-4.8 4.2 1.4 6.2L15 19.6 9.5 22.8l1.4-6.2-4.8-4.2 6.3-.6z" fill="#e8d8b4"/></svg>
    Limiteds</div>
  <div class="abs tile" style="left:494px;background:var(--red);color:var(--cream)">
    <i class="dot" style="left:8px;top:8px"></i><i class="dot" style="right:8px;top:8px"></i><i class="dot" style="left:8px;bottom:8px"></i><i class="dot" style="right:8px;bottom:8px"></i>
    <svg width="30" height="30" viewBox="0 0 30 30"><path d="M19 3a7 7 0 0 0-6.3 9.6L3 22.3 7.7 27l9.7-9.7A7 7 0 0 0 27 11l-4.2 4.2-5.3-1.4-1.4-5.3L20.3 4.3A7 7 0 0 0 19 3z" fill="#f1e5c9"/></svg>
    Customs</div>
  <div class="abs tile" style="left:730px;background:var(--cream);color:var(--ink)">
    <i class="dot" style="left:8px;top:8px"></i><i class="dot" style="right:8px;top:8px"></i><i class="dot" style="left:8px;bottom:8px"></i><i class="dot" style="right:8px;bottom:8px"></i>
    <svg width="32" height="28" viewBox="0 0 32 28"><path d="M6 11l3-8h14l3 8h3v12h-4v4h-4v-4H11v4H7v-4H3V11z" fill="#1f1f1f"/><circle cx="9" cy="16" r="2" fill="#e8d8b4"/><circle cx="23" cy="16" r="2" fill="#e8d8b4"/></svg>
    Classics</div>
  <div class="abs tile" style="left:965px;background:var(--green);color:var(--cream)">
    <i class="dot" style="left:8px;top:8px"></i><i class="dot" style="right:8px;top:8px"></i><i class="dot" style="left:8px;bottom:8px"></i><i class="dot" style="right:8px;bottom:8px"></i>
    <svg width="20" height="30" viewBox="0 0 20 30"><path d="M12 1L3 17h6l-2 12 10-17h-6z" fill="#e8d8b4"/></svg>
    Prototypes</div>
</section>

<section class="cmd">
  <div class="abs btn badge">Verified Station</div>
  <h2 class="abs display">Comman<br>der of the<br>Collector<br>Market</h2>
  <p class="abs lede">Every listing is vetted. 10,000+ Models Sold with 98% Positive Feedback.</p>
  <div class="abs feat" style="left:21px">
    <h4><svg width="18" height="20" viewBox="0 0 18 20"><path d="M9 1l8 3v6c0 5-3.5 8-8 9-4.5-1-8-4-8-9V4z" fill="#c9572b"/><path d="M5 10l3 3 5-6" fill="none" stroke="#1f1f1f" stroke-width="2"/></svg>Expert Vetting</h4>
    <p>Multi-point physical inspection for every auction item.</p>
  </div>
  <div class="abs feat" style="left:256px">
    <h4><svg width="18" height="20" viewBox="0 0 18 20"><path d="M9 1l8 3v6c0 5-3.5 8-8 9-4.5-1-8-4-8-9V4z" fill="#3f7a55"/></svg>Secure Escrow</h4>
    <p>Buyer protection guaranteed on every desert delivery.</p>
  </div>

  <div class="abs review r1">
    <div class="who"><div class="av" style="background:var(--ink);color:var(--cream)">GG</div>
      <div><div class="handle">@GEARS_N_GRAVEL</div><div class="role" style="color:var(--red)">Verified Collector</div></div></div>
    <div class="stars">★★★★★</div>
    <blockquote>"Found the missing 1992 Halvorsen tribute car here. Perfect condition, faster shipping than my last lap!"</blockquote>
  </div>
  <div class="abs review r2">
    <div class="who"><div class="av" style="background:var(--red);color:var(--cream)">CR</div>
      <div><div class="handle">@CANYONRUNNER_88</div><div class="role" style="color:#5e5d58">Elite Vendor</div></div></div>
    <div class="stars" style="color:var(--red)">★★★★★</div>
    <blockquote>"Sold my entire vintage collection in two days. The platform handle is rock solid and payouts are quick."</blockquote>
  </div>
</section>

<section class="garage">
  <h2 class="abs display">From the Garage</h2>
  <div class="abs sub">Built by collectors. Driven by passion.</div>
  <a class="abs btn btn-outline" style="left:1007px;top:115px;width:172px;height:31px;font-size:9px">Submit Your Build</a>

  <article class="abs post" style="left:21px;top:233px">
    <div class="abs ph" role="img" aria-label="Illuminated wall cabinet of collector cars" style="background:linear-gradient(180deg,#5a3418 0%,#8a5a30 35%,#3a2a1e 70%,#1c1612 100%)"></div>
    <div class="abs cap"><div class="cat">Collector Setups</div><h3>The JDM Archive Wall</h3></div>
  </article>
  <article class="abs post" style="left:316px;top:275px">
    <div class="abs ph" role="img" aria-label="Classic car model being restored on a workbench" style="background:linear-gradient(180deg,#2a2a28 0%,#5a5444 45%,#2a2824 75%,#161616 100%)"></div>
    <div class="abs cap"><div class="cat">Restoration Stories</div><h3>Reviving a '65 Legend</h3></div>
  </article>
  <article class="abs post" style="left:611px;top:233px">
    <div class="abs ph" role="img" aria-label="Red race car model with desert mesas behind" style="background:linear-gradient(180deg,#7a7672 0%,#8a6a56 35%,#6a2a24 62%,#1e1a18 100%)"></div>
    <div class="abs cap"><div class="cat">Top 10 Rare Finds</div><h3>Auction Week Highlights</h3></div>
  </article>
  <article class="abs post" style="left:906px;top:275px">
    <div class="abs ph" role="img" aria-label="Collector cars lined up in the desert under red rock cliffs" style="background:linear-gradient(180deg,#6a8ab0 0%,#b48a6a 30%,#a05a3a 50%,#c69a70 72%,#3a2a24 100%)"></div>
    <div class="abs cap"><div class="cat">Shop Meetups</div><h3>Arizona Desert Expo 2024</h3></div>
  </article>
</section>

<section class="join">
  <div class="abs corner"></div>
  <div class="abs shadow"></div>
  <div class="abs box">
    <div class="abs label kicker">Pit Crew Membership</div>
    <h2 class="abs display">Join the Pit Crew</h2>
    <p class="abs">Get first access to rare drops, members-only listings, and private auctions before they hit the open track.</p>
    <div class="abs field"><span>Signal your email...</span><b>SUBSCRIBE</b></div>
    <div class="abs perks">
      <span><svg width="10" height="10" viewBox="0 0 10 10"><circle cx="5" cy="5" r="5" fill="#2e5240"/><path d="M2.5 5l2 2 3-4" fill="none" stroke="#1f1f1f" stroke-width="1.3"/></svg>Early Access</span>
      <span><svg width="10" height="10" viewBox="0 0 10 10"><circle cx="5" cy="5" r="5" fill="#2e5240"/><path d="M2.5 5l2 2 3-4" fill="none" stroke="#1f1f1f" stroke-width="1.3"/></svg>No Spam Policy</span>
      <span><svg width="10" height="10" viewBox="0 0 10 10"><circle cx="5" cy="5" r="5" fill="#2e5240"/><path d="M2.5 5l2 2 3-4" fill="none" stroke="#1f1f1f" stroke-width="1.3"/></svg>Secret Drops</span>
    </div>
  </div>
</section>

<footer class="foot">
  <div class="abs fb">Brimble Diecast</div>
  <div class="abs copy">© 2026 — Built by Collectors</div>
  <nav class="abs links"><span>The Track</span><span>Shipping Log</span><span>Privacy</span><span>Terms</span></nav>
  <div class="abs social"><i></i><i></i><i></i></div>
</footer>

</body>
</html>
```